Tovrelan Ltda

Logo design focused on: - Construction of civil works - Electrical services - Metal structures - Equipment rental Tomás Ibarra Leiva Manager tovrelan.ltda@brevomail.example 56 9 48215037 Quelitoco s / n, Sorimar, San Pedro de Atacama

Building

Colors
33a6d7
0292cd
33b8a4
0555a3

```html
<!DOCTYPE html>
<html lang="en">
<head>
<meta charset="utf-8">
<title>Tovrelan Ltda — Business Card</title>
<link href="https://fonts.googleapis.com/css2?family=Open+Sans:wght@400;600&display=swap" rel="stylesheet">
<style>
  :root {
    --page-bg: #ece9e4;
    --kraft: #c7a67c;
    --kraft-light: #d0b189;
    --ink: #111111;
    --rule: rgba(17, 17, 17, 0.45);
  }
  * { margin: 0; padding: 0; box-sizing: border-box; }
  html, body {
    width: 1200px;
    height: 900px;
    overflow: hidden;
    background: var(--page-bg);
    font-family: "Open Sans", Arial, sans-serif;
    color: var(--ink);
  }
  .canvas { position: relative; width: 1200px; height: 900px; }

  .card {
    position: absolute;
    background: linear-gradient(135deg, var(--kraft-light), var(--kraft));
    box-shadow: 0 4px 14px rgba(0, 0, 0, 0.12);
  }

  /* Front: contact side */
  .card-front { left: 238px; top: 62px; width: 555px; height: 342px; }
  .brand-block {
    position: absolute;
    left: 80px; top: 103px;
    width: 156px;
    display: flex; flex-direction: column; align-items: center;
  }
  .brand-circle {
    width: 118px; height: 118px;
    border-radius: 50%;
    background: var(--ink);
  }
  .brand-block .brand-name {
    margin-top: 12px;
    font-size: 15px; font-weight: 600;
    letter-spacing: 0.08em;
    white-space: nowrap;
  }
  .divider {
    position: absolute;
    left: 270px; top: 90px;
    width: 1px; height: 170px;
    background: var(--rule);
  }
  .contact {
    position: absolute;
    left: 300px; top: 84px;
  }
  .person-name { font-size: 19px; font-weight: 600; line-height: 1.2; }
  .person-role { font-size: 14px; margin-top: 3px; }
  .address { font-size: 14px; line-height: 1.45; margin-top: 20px; }
  .lines { margin-top: 20px; font-size: 14px; line-height: 1.4; }
  .line { display: flex; align-items: center; gap: 8px; }
  .line svg { width: 11px; height: 11px; flex: none; }

  /* Back: brand side */
  .card-back { left: 458px; top: 518px; width: 559px; height: 342px; }
  .lockup {
    position: absolute;
    left: 110px; top: 122px;
    display: flex; align-items: center; gap: 16px;
  }
  .lockup .brand-circle { width: 64px; height: 64px; }
  .lockup .brand-name {
    font-size: 38px; font-weight: 400;
    letter-spacing: 0.06em;
    line-height: 1;
  }
  .services {
    position: absolute;
    left: 0; right: 0; top: 250px;
    text-align: center;
    font-size: 14.5px; font-weight: 600;
    line-height: 1.4;
  }
  .services .sep { padding: 0 8px; font-weight: 400; }
</style>
</head>
<body>
<main class="canvas">

  <section class="card card-front" aria-label="Business card, contact side">
    <div class="brand-block">
      <div class="brand-circle"></div>
      <span class="brand-name">TOVRELAN LTDA</span>
    </div>
    <div class="divider"></div>
    <div class="contact">
      <p class="person-name">Tomás Ibarra Leiva</p>
      <p class="person-role">Manager</p>
      <p class="address">Quelitoco s / n, Sorimar,<br>San Pedro de Atacama</p>
      <div class="lines">
        <p class="line">
          <svg viewBox="0 0 24 24" aria-hidden="true"><path fill="currentColor" d="M6.6 10.8a15.1 15.1 0 0 0 6.6 6.6l2.2-2.2c.3-.3.7-.4 1-.2 1.1.4 2.3.6 3.6.6.6 0 1 .4 1 1V20c0 .6-.4 1-1 1A17 17 0 0 1 3 4c0-.6.4-1 1-1h3.5c.6 0 1 .4 1 1 0 1.3.2 2.5.6 3.6.1.3 0 .7-.2 1z"/></svg>
          <span>56 9 48215037</span>
        </p>
        <p class="line">
          <svg viewBox="0 0 24 24" aria-hidden="true"><path fill="currentColor" d="M2 5h20v14H2z"/><path fill="none" stroke="#c7a67c" stroke-width="1.8" d="M2.5 5.5 12 13l9.5-7.5"/></svg>
          <span>tovrelan.ltda@brevomail.example</span>
        </p>
      </div>
    </div>
  </section>

  <section class="card card-back" aria-label="Business card, brand side">
    <div class="lockup">
      <div class="brand-circle"></div>
      <span class="brand-name">TOVRELAN Ltda</span>
    </div>
    <div class="services">
      <p>Construction of Civil Works<span class="sep">|</span>Electrical Services</p>
      <p>Metal Structures<span class="sep">|</span>Equipment Rental</p>
    </div>
  </section>

</main>
</body>
</html>
```